Velmora Water Purification

We need a website set up on a "Free account" WordPress platform. (This is the type of Wordpress site that you can sign up for and create online for free (not a server-hosted type.)
The website will be for a water purification company. They install devices in homes to purify the water for safer drinking, bathing, and cleaning.
Our logo is attached. Please keep color scheme of the website consistent with the logo.
Water Purification

```html
<!DOCTYPE html>
<html lang="en">
<head>
<meta charset="utf-8">
<title>Velmora Water Purification</title>
<link rel="stylesheet" href="https://fonts.googleapis.com/css2?family=Open+Sans:wght@400;600;700&display=swap">
<style>
  :root {
    --brand-blue: #0b6fc0;
    --deep-blue: #0a5ea8;
    --text-blue: #1866ad;
    --nav-light: #2a78bd;
    --cyan: #18a9e0;
    --page-bg: #f5f5f5;
    --white: #ffffff;
    --dot-dark: #2f3a44;
    --border: #dcdcdc;
  }
  * { box-sizing: border-box; margin: 0; padding: 0; }
  html, body { width: 949px; height: 1200px; overflow: hidden; }
  body {
    position: relative;
    background: var(--page-bg);
    font-family: "Open Sans", Arial, sans-serif;
    color: var(--text-blue);
  }
  .abs { position: absolute; }

  /* Header */
  .contact-line { top: 17px; font-size: 11px; font-weight: 400; color: var(--deep-blue); display: flex; align-items: center; gap: 4px; white-space: nowrap; }
  .contact-line b { color: var(--cyan); font-weight: 600; }
  .contact-line svg { width: 11px; height: 11px; }
  .search-box { left: 742px; top: 14px; width: 156px; height: 31px; background: var(--white); border: 1px solid var(--border); font-size: 12px; color: #b5b5b5; padding: 7px 11px; }
  .search-box svg { position: absolute; right: 8px; top: 6px; width: 18px; height: 18px; }
  .brand { left: 84px; top: 48px; display: flex; align-items: center; gap: 8px; }
  .brand-mark { width: 20px; height: 20px; border-radius: 50%; background: var(--deep-blue); }
  .brand-name { font-size: 15px; font-weight: 700; color: var(--deep-blue); line-height: 1.15; width: 110px; }
  .main-nav { left: 262px; top: 81px; display: flex; gap: 23px; font-size: 14px; font-weight: 600; color: var(--deep-blue); white-space: nowrap; }
  .main-nav .active { color: var(--nav-light); }

  /* Hero */
  .hero { left: 0; top: 128px; width: 949px; height: 430px; }
  .hero-photo { position: absolute; inset: 0; background: linear-gradient(100deg, #c9d9e8 0%, #a9c3dc 30%, #b8cfe4 55%, #cfdcea 100%); }
  .hero-wave { position: absolute; left: 0; bottom: 0; width: 949px; height: 60px; }
  .hero-title { left: 490px; top: 182px; width: 355px; text-align: center; font-size: 54px; font-weight: 700; line-height: 56px; color: var(--deep-blue); letter-spacing: 0.5px; }
  .hero-sub { left: 537px; top: 383px; width: 260px; text-align: center; font-size: 21px; line-height: 28.5px; color: var(--white); }
  .arrow { top: 340px; width: 26px; height: 48px; }

  /* Slider dots */
  .dots { left: 397px; top: 571px; display: flex; gap: 13px; }
  .dots span { width: 14px; height: 14px; border-radius: 50%; background: var(--brand-blue); }
  .dots .current { background: var(--dot-dark); }

  /* Feature columns */
  .feature { top: 626px; width: 277px; }
  .feature h2 { text-align: center; font-size: 17.5px; font-weight: 700; color: var(--deep-blue); margin-bottom: 7px; }
  .feature-photo { width: 100%; height: 171px; }
  .photo-facilities { background: linear-gradient(160deg, #e8edf0, #c7d2db 60%, #9fb4c6); }
  .photo-technology { background: linear-gradient(100deg, #6d737b 0%, #2c3a6c 35%, #dcdfe2 65%, #b8bcc1 100%); }
  .photo-plant { background: linear-gradient(170deg, #6d8f3e, #7d9a5a 50%, #8a9a88); }

  /* Info text */
  .info { left: 58px; top: 864px; width: 840px; }
  .info h3 { font-size: 13.5px; font-weight: 700; color: var(--cyan); margin-bottom: 2px; }
  .info p { font-size: 9.8px; line-height: 12.4px; color: var(--text-blue); margin-bottom: 12px; }
  .info .section + .section { margin-top: 14px; }

  /* Footer */
  .site-footer { left: 0; top: 1088px; width: 949px; height: 112px; background: var(--brand-blue); color: var(--white); }
  .footer-nav { position: absolute; left: 63px; top: 17px; display: flex; gap: 17px; font-size: 9.6px; }
  .social { position: absolute; top: 14px; display: block; width: 19px; height: 19px; border-radius: 50%; background: var(--white); }
  .legal { position: absolute; top: 65px; font-size: 8.4px; white-space: nowrap; }
</style>
</head>
<body>

<header>
  <div class="contact-line abs" style="left:84px">
    <svg viewBox="0 0 12 12"><circle cx="6" cy="6" r="6" fill="#18a9e0"/><path d="M3 6.2l2 2 4-4" stroke="#fff" stroke-width="1.6" fill="none"/></svg>
    Main Office: <b>0 800 555 0142</b>
  </div>
  <div class="contact-line abs" style="left:266px">
    <svg viewBox="0 0 12 12"><circle cx="6" cy="6" r="6" fill="#18a9e0"/><path d="M3 6.2l2 2 4-4" stroke="#fff" stroke-width="1.6" fill="none"/></svg>
    International: <b>000 800 555 0199</b>
  </div>
  <div class="search-box abs">Search
    <svg viewBox="0 0 20 20"><circle cx="8" cy="8" r="6" stroke="#c4c4c4" stroke-width="2" fill="none"/><path d="M12.5 12.5l6 6" stroke="#c4c4c4" stroke-width="2.4"/></svg>
  </div>
  <div class="brand abs">
    <span class="brand-mark"></span>
    <span class="brand-name">Velmora Water Purification</span>
  </div>
  <nav class="main-nav abs">
    <span>Applications</span><span>Solutions</span><span class="active">Industries</span><span>Safety &amp;Health</span><span>Innovations</span><span>About</span><span>Contact</span>
  </nav>
</header>

<section class="hero abs">
  <div class="hero-photo" role="img" aria-label="Glass of clear drinking water with splashing water on a soft blue background"></div>
  <svg class="hero-wave" viewBox="0 0 949 60" preserveAspectRatio="none">
    <path d="M0 22 C120 36 220 10 330 24 C440 38 520 44 600 26 C690 6 800 10 949 20 L949 60 L0 60 Z" fill="#f5f5f5"/>
  </svg>
</section>
<h1 class="hero-title abs">PURIFIED DRINKING WATER</h1>
<p class="hero-sub abs">Bringing Clean Drinking Water to every person around the World.</p>
<svg class="arrow abs" style="left:54px" viewBox="0 0 26 48"><path d="M23 3L4 24l19 21" stroke="#0b6fc0" stroke-width="2.5" fill="none"/></svg>
<svg class="arrow abs" style="left:873px" viewBox="0 0 26 48"><path d="M3 3l19 21L3 45" stroke="#0b6fc0" stroke-width="2.5" fill="none"/></svg>

<div class="dots abs"><span></span><span></span><span></span><span class="current"></span><span></span></div>

<section class="feature abs" style="left:58px">
  <h2>FACILITIES</h2>
  <div class="feature-photo photo-facilities" role="img" aria-label="Indoor water treatment facility with rows of white filtration pipes"></div>
</section>
<section class="feature abs" style="left:340px">
  <h2>TECHNOLOGY</h2>
  <div class="feature-photo photo-technology" role="img" aria-label="Close view of reverse osmosis membrane housings beside a blue tank"></div>
</section>
<section class="feature abs" style="left:622px">
  <h2>PLANT SITE</h2>
  <div class="feature-photo photo-plant" role="img" aria-label="Aerial view of a water treatment plant surrounded by green fields"></div>
</section>

<main class="info abs">
  <div class="section">
    <h3>WATER QUALITY</h3>
    <p>The United States has one of the safest water supplies in the world. If you are among the 286 million Americans that get their water from a community water system (1), your tap water is regulated by the United States Environmental Protection Agency (EPA). Drinking water varies from place to place, depending on the condition of the source water from which it is drawn and the treatment it receives, but it must meet EPA regulations.</p>
  </div>
  <div class="section">
    <h3>REGULATIONS</h3>
    <p>The Safe Drinking Water Act (SDWA) was passed by Congress in 1974, with subsequent amendments in 1986 and 1996, to ensure and protect the quality of Americans' drinking water. Under SDWA, the United States Environmental Protection Agency (EPA) is given authority to set the standards for drinking water quality and oversee states, localities, and water suppliers who implement those standards.</p>
    <p>Through the SDWA, all public water systems in the United States need to follow the standards and regulations set by the EPA. The EPA has set maximum contaminant levels and/or treatment technique requirements for over 90 different contaminants in public drinking water, including microorganisms, disinfectants, disinfections by-products, inorganic chemicals, organic chemicals, and radionuclides</p>
  </div>
</main>

<footer class="site-footer abs">
  <nav class="footer-nav">
    <span>Applications</span><span>Solutions</span><span>Industries</span><span>Safety &amp;Health</span><span>Innovations</span><span>About</span><span>Contact</span>
  </nav>
  <span class="social" style="left:801px" aria-label="Social link"></span>
  <span class="social" style="left:836px" aria-label="Social link"></span>
  <span class="social" style="left:873px" aria-label="Social link"></span>
  <p class="legal" style="left:227px">Contact Us | Our Mission | Terms &amp; Conditions</p>
  <p class="legal" style="left:450px">Velmora Water ©2017 All Rights Reserved | 1590412267.3071s</p>
</footer>

</body>
</html>
```